New fresh farmers market needs a Wordpress theme

We need a wordpress theme for the web site for a new farmers market in Perth, Western Australia called "Copper Ridge Farmers Market". The market operates weekly on Sunday mornings and is set within beautiful grass and native bush surroundings. Copper Ridge is a heritage listed historical site where one of the first communications towers was built in Perth.
We already have a logo and business cards which I've attached to this project. They should really accelerate colour selection etc. There are also many photos of the area already on Google (search for Copper Ridge, Perth Western Australia).
I already have a freshly installed Wordpress site and can supply credentials for deployment if that's in scope.
Deliverables are:
1. Wordpress theme
2. Starter page where you can register interest / join a mailing list

```html
<!DOCTYPE html>
<html lang="en">
<head>
<meta charset="utf-8">
<title>Copper Ridge Farmers Market</title>
<link rel="stylesheet" href="https://fonts.googleapis.com/css2?family=Lora:wght@400;700&family=Raleway:wght@400;600&display=swap">
<style>
  :root {
    --green-bright: #6cb344;
    --green-deep: #5a8c3a;
    --white: #ffffff;
    --nav-grey: #666666;
    --ink: #111111;
    --veil: rgba(255,255,255,0.75);
  }
  * { box-sizing: border-box; margin: 0; padding: 0; }
  html, body { width: 1200px; height: 721px; overflow: hidden; background: var(--white); }
  body { position: relative; font-family: "Lora", Georgia, serif; }

  .top-bar {
    position: absolute; left: 0; top: 0; width: 1200px; height: 36px;
    background: var(--green-bright); color: var(--white);
    font-weight: 700; font-size: 14.5px; letter-spacing: 0.3px;
  }
  .top-contact { position: absolute; left: 120px; top: 9px; display: flex; gap: 18px; align-items: center; }
  .top-contact span { display: flex; align-items: center; gap: 4px; }
  .top-links { position: absolute; right: 121px; top: 7px; display: flex; gap: 18px; }

  .site-header { position: absolute; left: 0; top: 36px; width: 1200px; height: 101px; background: var(--white); }
  .brand { position: absolute; left: 128px; top: 4px; width: 112px; text-align: center; color: #555; font-family: "Raleway", Arial, sans-serif; font-weight: 600; }
  .brand-mark { display: block; margin: 0 auto 3px; width: 58px; height: 58px; border-radius: 50%; border: 4px solid #555; }
  .brand-name { font-size: 18px; line-height: 18px; }
  .brand-sub { font-size: 12px; line-height: 14px; }
  .main-nav { position: absolute; right: 113px; top: 41px; display: flex; gap: 24px; align-items: center; color: var(--nav-grey); font-size: 15px; letter-spacing: 0.5px; }

  .hero {
    position: absolute; left: 0; top: 137px; width: 1200px; height: 477px;
    background:
      linear-gradient(180deg, #b7403a 0%, #4b5a2c 6%, #3c6b2a 30%, #5a8a36 55%, #3f7a2c 72%, #6a9c3e 100%);
  }
  .hero-produce {
    position: absolute; inset: 0;
    background: linear-gradient(90deg, rgba(90,50,90,0.45) 0%, rgba(0,0,0,0) 20%, rgba(220,110,40,0.35) 42%, rgba(0,0,0,0) 55%, rgba(0,0,0,0) 70%, rgba(230,220,190,0.3) 85%, rgba(0,0,0,0) 100%);
  }
  .hero-spinner { position: absolute; left: 587px; top: 331px; }
  .hero-title {
    position: absolute; left: 330px; top: 370px; width: 543px; height: 67px;
    background: var(--veil); color: var(--ink);
    font-family: "Raleway", Arial, sans-serif; font-size: 36px; font-weight: 400;
    display: flex; align-items: center; justify-content: center;
  }

  .site-footer { position: absolute; left: 0; top: 671px; width: 1200px; height: 50px; background: var(--green-deep); color: var(--white); }
  .copyright { position: absolute; left: 120px; top: 17px; font-size: 13.5px; font-weight: 700; }
  .social { position: absolute; right: 121px; top: 18px; display: flex; gap: 20px; }
  .social span { width: 13px; height: 13px; border-radius: 50%; background: var(--white); }
</style>
</head>
<body>
  <div class="top-bar">
    <div class="top-contact">
      <span>
        <svg width="12" height="12" viewBox="0 0 24 24" fill="#fff"><path d="M6.6 10.8a15 15 0 0 0 6.6 6.6l2.2-2.2c.3-.3.7-.4 1-.2 1.1.4 2.3.6 3.6.6.6 0 1 .4 1 1V20c0 .6-.4 1-1 1A17 17 0 0 1 3 4c0-.6.4-1 1-1h3.5c.6 0 1 .4 1 1 0 1.3.2 2.5.6 3.6.1.3 0 .7-.2 1z"/></svg>
        0400 555 123
      </span>
      <span>
        <svg width="14" height="11" viewBox="0 0 24 18" fill="#fff"><path d="M0 0h24v18H0z" fill="none"/><path d="M0 1l12 8 12-8V0H0zM0 3.5V18h24V3.5l-12 8z"/></svg>
        manager@copperridgefarmersmarket.com.au
      </span>
    </div>
    <nav class="top-links"><span>Media</span><span>News &amp; Events</span><span>Subscribe</span></nav>
  </div>

  <header class="site-header">
    <div class="brand">
      <span class="brand-mark"></span>
      <div class="brand-name">Copper Ridge</div>
      <div class="brand-sub">Farmers Market</div>
    </div>
    <nav class="main-nav">
      <span>Home</span><span>Stallholders</span><span>Sponsors</span><span>About Us</span><span>Location</span><span>Contact Us</span>
      <svg width="16" height="16" viewBox="0 0 16 16" fill="none" stroke="#666" stroke-width="1.4"><circle cx="9" cy="6.5" r="5"/><path d="M5.5 10 1 14.5"/></svg>
    </nav>
  </header>

  <section class="hero" role="img" aria-label="Photograph of fresh vegetables stacked on market shelves with price cards">
    <div class="hero-produce"></div>
    <svg class="hero-spinner" width="24" height="24" viewBox="0 0 24 24" fill="none" stroke="#fff" stroke-width="1.5"><path d="M20 12a8 8 0 1 1-4-6.9"/><path d="M16 2v4h-4"/></svg>
    <h1 class="hero-title">Copper Ridge Farmers Market</h1>
  </section>

  <footer class="site-footer">
    <p class="copyright">Copyright © 2017 Copper Ridge Farmers Market. All Rights Reserved.</p>
    <div class="social"><span></span><span></span><span></span></div>
  </footer>
</body>
</html>
```